Personal Development Brand Needs a Workbook Cover Design

We need a clean and sleek cover design for our A4-Sized workbook called the "Lantern Path Journal Set"

There's around 90 pages in the workbook, if that matters for the spine.

Necessary Elements on the Front Cover:

- Logo
- Title: Keen Crest Lantern Path Journal
- Subtitle: A Simple Workbook to Track Your Transformation
- Author Name: Dorian Pellow

Elements on Back Cover:

- The Keen Crest Charter

```html
<!DOCTYPE html>
<html lang="en">
<head>
<meta charset="utf-8">
<title>Keen Crest Lantern Path Journal – Cover</title>
<link href="https://fonts.googleapis.com/css2?family=Montserrat:wght@700;800&family=Questrial&display=swap" rel="stylesheet">
<style>
  :root{
    --bg:#d6dde3;
    --red:#e3392b;
    --red-soft:#ee6a5e;
    --red-tint:#f28b80;
    --navy:#2f3b46;
    --slate:#525b63;
    --white:#ffffff;
    --grey-text:#7c8790;
    --rule:#c9ced2;
  }
  *{margin:0;padding:0;box-sizing:border-box}
  html,body{width:1200px;height:1200px;overflow:hidden;background:var(--bg)}
  .canvas{position:relative;width:1200px;height:1200px}
  .cover{position:absolute;left:66px;top:238px;width:1068px;height:722px;display:flex}

  /* back cover */
  .back{position:relative;width:511px;height:722px;background:var(--red)}
  .back__panel{position:absolute;left:36px;top:40px;width:439px;height:643px;background:var(--navy);padding:44px 30px 0}
  .charter__title{font-family:"Montserrat",sans-serif;font-weight:800;font-size:19px;color:var(--white);margin-bottom:20px}
  .charter__title span{color:var(--red)}
  .charter__item{font-family:"Questrial",sans-serif;font-size:18px;line-height:23px;color:var(--white);margin-bottom:22px;position:relative;padding-bottom:6px}
  .charter__item::after{content:"";position:absolute;left:0;bottom:-4px;width:119px;height:3px;background:var(--red)}
  .brand{font-family:"Montserrat",sans-serif;font-weight:800;color:var(--white);letter-spacing:-0.5px}
  .back .brand{position:absolute;left:0;right:0;top:596px;text-align:center;font-size:20px}

  /* spine */
  .spine{position:relative;width:46px;height:722px;background:var(--navy)}
  .spine .brand{position:absolute;left:50%;top:356px;font-size:19px;transform:translate(-50%,-50%) rotate(-90deg);white-space:nowrap}

  /* front cover */
  .front{position:relative;width:511px;height:722px;background:var(--white);overflow:hidden}
  .front__photo{position:absolute;left:0;top:0}
  .front__logo-box{position:absolute;left:274px;top:0;width:217px;height:106px;background:var(--slate);display:flex;align-items:center;justify-content:center}
  .front__logo-box .brand{font-size:30px}
  .front__tag{position:absolute;left:274px;top:106px;width:217px;height:324px;background:var(--red);opacity:.82}
  .front__tag-text{position:absolute;left:274px;top:190px;width:217px;height:134px;display:flex;align-items:center;justify-content:center;text-align:center;font-family:"Montserrat",sans-serif;font-weight:800;font-size:22px;line-height:30px;color:var(--red-tint);border-top:3px solid var(--red-tint);border-bottom:3px solid var(--red-tint);margin-left:20px;width:177px;padding:0}
  .title{position:absolute;left:13px;top:392px;font-family:"Montserrat",sans-serif;font-weight:800;font-size:48px;line-height:61px;color:var(--navy);letter-spacing:-1px}
  .title span{color:var(--red)}
  .title__rule{position:absolute;left:23px;top:585px;width:450px;height:2px;background:var(--rule)}
  .subtitle{position:absolute;left:14px;top:594px;font-family:"Questrial",sans-serif;font-size:19px;color:var(--grey-text);white-space:nowrap}
  .subtitle strong{font-family:"Montserrat",sans-serif;font-weight:800;font-size:18px;color:var(--grey-text)}
  .author{position:absolute;left:42px;top:646px;width:203px;height:76px;background:var(--red);padding:22px 0 0 19px}
  .author__name{font-family:"Montserrat",sans-serif;font-weight:800;font-size:22px;color:var(--white);letter-spacing:-0.3px}
  .author__name u{text-decoration:none;border-bottom:2px solid var(--white);padding-bottom:2px}
</style>
</head>
<body>
<div class="canvas">
  <div class="cover">
    <section class="back">
      <div class="back__panel">
        <h2 class="charter__title"><span>T</span>he <span>K</span>een <span>C</span>rest <span>C</span>harter</h2>
        <p class="charter__item">We do things that matter.</p>
        <p class="charter__item">We are skeptical of our limits.</p>
        <p class="charter__item">We don't fear mistakes, only mediocrity.</p>
        <p class="charter__item">We don't just think positive thoughts,<br>we act on them.</p>
        <p class="charter__item">We know our most important skill is the ability<br>to dream beyond our current abilities.</p>
        <div class="brand">KeenCrest</div>
      </div>
    </section>

    <section class="spine">
      <div class="brand">KeenCrest</div>
    </section>

    <section class="front">
      <svg class="front__photo" width="511" height="414" viewBox="0 0 511 414" role="img" aria-label="Photo of a cyclist in grey kit riding a road bike along a guardrail">
        <defs>
          <linearGradient id="photoTone" x1="0" y1="0" x2="1" y2="1">
            <stop offset="0" stop-color="#8d9599"/>
            <stop offset=".5" stop-color="#5e6763"/>
            <stop offset="1" stop-color="#6f7a6a"/>
          </linearGradient>
        </defs>
        <polygon points="0,0 511,0 511,414 0,246" fill="url(#photoTone)"/>
      </svg>
      <div class="front__logo-box"><span class="brand">KeenCrest</span></div>
      <div class="front__tag"></div>
      <div class="front__tag-text">Keen Crest<br>Lantern Path<br>Journal</div>

      <h1 class="title"><span>K</span>een Crest<br><span>L</span>antern Path<br><span>J</span>ournal</h1>
      <div class="title__rule"></div>
      <p class="subtitle">A Simple Workbook to <strong>Track Your Transformation</strong></p>
      <div class="author"><p class="author__name"><u>Dorian</u> Pellow</p></div>
    </section>
  </div>
</div>
</body>
</html>
```